New boutique hotel for tourists, with hint of art deco styling

This is a new, soon to be completed, boutique hotel in Sydney. A letterhead with a logo is required. Less emphasis on the word "boutique". Perhaps the word could be screened to be lighter in colour (or print intensity). Would like a simple, clear, easy-to read, sans serif type face. The information on the letterhead is:
Mrs Fennel Boutique Hotel
417 Larkmoor Street,
Wellbrook, NSW, 2094
Australia
Tel: +61 2 9704-5512
mrsfennelhotel@example-mail.com
mrsfennelhotel.example.au
ABN 47 902 365 148

Target Market(s)

travellers, tourists, various ages

Industry/Entity Type

Hospitality

Contact Information for Business Card

Mrs Fennel Boutique Hotel
417 Larkmoor Street,
Wellbrook, NSW, 2097
Telephone: (02) 9704-5512
www.mrsfennelhotel.example.au
mrsfennelhotel@example-mail.com
ABN 47 902 365 148

Logo Text

suggest playing with the letter "B"

Font styles to use
Sans Serif

Colors
3176b5

Requirements
Must have
• ABN to be very small.
• Must be clear, easy to read and in a sans serif typeface, please!
Nice to have
• The word "Boutique" should be less intense in appearance to the rest of the name, or even "Boutique Hotel" can have less prominence than "Mrs Fennel".
Should not have
• No serif typeface. Sans serif only will be accepted.

```html
<!DOCTYPE html>
<html lang="en">
<head>
<meta charset="utf-8">
<title>Mrs Fennel Boutique Hotel – Letterhead</title>
<link rel="stylesheet" href="https://fonts.googleapis.com/css2?family=Questrial&display=swap">
<style>
  :root {
    --brand-blue: #2b77b7;
    --brand-blue-light: #5f9ccf;
    --paper: #ffffff;
    --footer-text: #ffffff;
  }
  * { margin: 0; padding: 0; box-sizing: border-box; }
  html, body {
    width: 848px;
    height: 1200px;
    overflow: hidden;
    background: var(--paper);
  }
  .letterhead {
    position: relative;
    width: 848px;
    height: 1200px;
    background: var(--paper);
    font-family: "Questrial", sans-serif;
    overflow: hidden;
  }
  .brand {
    position: absolute;
    left: 252px;
    top: 60px;
    display: flex;
    align-items: center;
    gap: 14px;
  }
  .brand-square {
    width: 56px;
    height: 74px;
    background: var(--brand-blue);
  }
  .brand-text { display: flex; flex-direction: column; }
  .brand-name {
    color: var(--brand-blue);
    font-size: 42px;
    line-height: 1;
    letter-spacing: -0.5px;
  }
  .brand-tagline {
    color: var(--brand-blue-light);
    font-size: 17px;
    letter-spacing: 2.4px;
    margin-top: 6px;
    margin-left: 10px;
  }
  .footer {
    position: absolute;
    left: 0;
    top: 997px;
    width: 848px;
    height: 203px;
    background: var(--brand-blue);
    color: var(--footer-text);
  }
  .footer-name {
    position: absolute;
    left: 31px;
    top: 20px;
    font-size: 32px;
    letter-spacing: -0.5px;
  }
  .contact-list {
    position: absolute;
    top: 74px;
    list-style: none;
    font-size: 22px;
    line-height: 29px;
    letter-spacing: 0.4px;
  }
  .contact-list--digital { left: 31px; font-size: 19px; letter-spacing: 0.2px; }
  .contact-list--address { left: 358px; }
  .abn {
    position: absolute;
    right: 37px;
    top: 145px;
    font-size: 14px;
  }
</style>
</head>
<body>
  <main class="letterhead">
    <header class="brand">
      <div class="brand-square" aria-hidden="true"></div>
      <div class="brand-text">
        <span class="brand-name">Mrs Fennel</span>
        <span class="brand-tagline">BOUTIQUE HOTEL</span>
      </div>
    </header>

    <footer class="footer">
      <div class="footer-name">Mrs Fennel</div>
      <ul class="contact-list contact-list--digital">
        <li>mrsfennelhotel@example-mail.com</li>
        <li>mrsfennelhotel.example.au</li>
        <li>Tel: +61 2 9704-5512</li>
      </ul>
      <ul class="contact-list contact-list--address">
        <li>417 Larkmoor Street</li>
        <li>Wellbrook,NSW,2094</li>
        <li>Australia</li>
      </ul>
      <div class="abn">ABN 47 902 365 148</div>
    </footer>
  </main>
</body>
</html>
```